Upgrade UI for an existing app

I have an app that is already in the appstore, and I have finally get to the point where the app is fairly complete in its user flow and app features.

I would like to take the app to the next level, and completely revamp its look and feel, to give it that flat iOS7 look.

The app can be downloaded at https://apps.vendrulo.example/us/app/brindle-kto/id574093186?mt=8

And you can log into the app using the credential below:

sketch.harbor
password

I am also open to new ideas around UX, but my biggest focus is on getting the UI updated, especially for the setting page, support page, and about page.

Thanks,

Rob

Majority of the submissions are for iPhone, whereas I was hoping for more iPad redesign.

I think the issue is that, a lot of people didn't download the app from appstore.

I have uploaded two zip files with iPad screenshot.  Please submit a few designs that are based off the existing iPad screenshot.

```html
<!DOCTYPE html>
<html lang="en">
<head>
<meta charset="utf-8">
<title>My Exams</title>
<link rel="stylesheet" href="https://fonts.googleapis.com/css2?family=Lato:wght@300;400;700&display=swap">
<style>
  :root {
    --brand-green: #28d08d;
    --white: #ffffff;
    --title-ink: #2e3a3e;
    --muted-ink: #a8b0ae;
    --accent-red: #e8323f;
    --card-fill: rgba(255, 255, 255, 0.72);
    --card-shade: rgba(90, 110, 60, 0.18);
  }
  * { box-sizing: border-box; margin: 0; padding: 0; }
  html, body { width: 676px; height: 1200px; overflow: hidden; background: var(--white); }
  body { font-family: "Lato", "Helvetica Neue", Arial, sans-serif; }

  .screen {
    position: absolute; left: 0; top: 0;
    width: 640px; height: 1136px;
    transform: scale(1.05625); transform-origin: 0 0;
    overflow: hidden;
  }
  .backdrop {
    position: absolute; inset: 0;
    background:
      radial-gradient(ellipse 420px 300px at 600px 160px, #9ecfe6 0%, rgba(158,207,230,0) 70%),
      radial-gradient(ellipse 500px 260px at 120px 150px, #dfeeee 0%, rgba(223,238,238,0) 80%),
      radial-gradient(ellipse 380px 260px at 40px 650px, #b5d66e 0%, rgba(181,214,110,0) 75%),
      radial-gradient(ellipse 360px 240px at 640px 760px, #8fb83c 0%, rgba(143,184,60,0) 75%),
      radial-gradient(ellipse 420px 200px at 320px 980px, #e3e28e 0%, rgba(227,226,142,0) 75%),
      linear-gradient(180deg, #cfe6e3 0%, #c9dfb0 40%, #b9d47a 70%, #a8c44c 100%);
  }

  .app-bar {
    position: absolute; left: 0; top: 0; width: 640px; height: 128px;
    background: var(--brand-green); color: var(--white);
  }
  .status-bar { position: absolute; left: 0; top: 0; width: 640px; height: 40px; font-size: 22px; }
  .status-bar .carrier { position: absolute; left: 12px; top: 7px; display: flex; align-items: center; gap: 6px; }
  .signal { display: flex; gap: 3px; }
  .signal i { width: 11px; height: 11px; border-radius: 50%; border: 1.5px solid var(--white); }
  .signal i.on { background: var(--white); }
  .status-bar .clock { position: absolute; left: 0; right: 0; top: 7px; text-align: center; font-weight: 700; }
  .status-bar .power { position: absolute; right: 10px; top: 7px; display: flex; align-items: center; gap: 10px; }
  .battery { width: 46px; height: 20px; border: 2px solid var(--white); border-radius: 3px; padding: 2px; position: relative; }
  .battery::after { content: ""; position: absolute; right: -5px; top: 5px; width: 3px; height: 6px; background: var(--white); }
  .battery span { display: block; width: 100%; height: 100%; background: var(--white); }

  .menu-button { position: absolute; left: 24px; top: 56px; width: 50px; height: 50px; }
  .page-title {
    position: absolute; left: 0; right: 0; top: 54px; text-align: center;
    font-size: 42px; font-weight: 300; letter-spacing: 0.3px;
  }

  .exam-list { position: absolute; left: 18px; top: 148px; width: 603px; list-style: none; }
  .exam-card {
    position: absolute; left: 0; width: 603px; height: 120px;
    background: var(--card-fill);
    box-shadow: 0 2px 2px var(--card-shade);
  }
  .progress-ring { position: absolute; left: 9px; top: 10px; width: 100px; height: 100px; }
  .progress-value {
    position: absolute; left: 9px; top: 10px; width: 100px; height: 100px;
    display: flex; align-items: center; justify-content: center;
    color: var(--accent-red); font-size: 19px; font-weight: 400;
  }
  .exam-title { position: absolute; left: 122px; top: 24px; font-size: 23.5px; font-weight: 400; color: var(--title-ink); white-space: nowrap; }
  .exam-status { position: absolute; left: 122px; top: 60px; font-size: 18px; font-weight: 300; color: var(--muted-ink); white-space: nowrap; }
  .exam-action { position: absolute; left: 528px; top: 30px; width: 50px; height: 60px; }
</style>
</head>
<body>
<svg width="0" height="0" style="position:absolute" aria-hidden="true">
  <defs>
    <linearGradient id="arc-fill" x1="0" y1="0" x2="1" y2="0">
      <stop offset="0" stop-color="#3fd10a"/>
      <stop offset="1" stop-color="#d4f200"/>
    </linearGradient>
    <radialGradient id="ring-base" cx="0.5" cy="0.4" r="0.6">
      <stop offset="0.6" stop-color="#f6f5f2"/>
      <stop offset="1" stop-color="#dcdbd7"/>
    </radialGradient>
    <filter id="disc-shadow" x="-20%" y="-20%" width="140%" height="150%">
      <feDropShadow dx="0" dy="2" stdDeviation="2" flood-color="#000" flood-opacity="0.22"/>
    </filter>
    <symbol id="ring" viewBox="0 0 100 100">
      <circle cx="50" cy="50" r="48" fill="url(#ring-base)"/>
      <circle cx="50" cy="50" r="35" fill="#ffffff" filter="url(#disc-shadow)"/>
    </symbol>
    <symbol id="chevron" viewBox="0 0 50 60">
      <path d="M18 10 L40 30 L18 50" fill="none" stroke="#e8323f" stroke-width="2"/>
    </symbol>
    <symbol id="download" viewBox="0 0 50 60">
      <path d="M17 14 H5 V54 H45 V14 H33" fill="none" stroke="#e8323f" stroke-width="2"/>
      <path d="M25 2 V40 M14 29 L25 40 L36 29" fill="none" stroke="#e8323f" stroke-width="2"/>
    </symbol>
  </defs>
</svg>

<main class="screen">
  <div class="backdrop"></div>

  <header class="app-bar">
    <div class="status-bar">
      <div class="carrier">
        <span class="signal"><i class="on"></i><i class="on"></i><i class="on"></i><i></i><i></i></span>
        <span>VELA</span>
        <svg width="24" height="18" viewBox="0 0 24 18" aria-hidden="true">
          <path d="M2 6 A14 14 0 0 1 22 6" fill="none" stroke="#fff" stroke-width="2.4"/>
          <path d="M6 10 A8.5 8.5 0 0 1 18 10" fill="none" stroke="#fff" stroke-width="2.4"/>
          <circle cx="12" cy="15" r="2.4" fill="#fff"/>
        </svg>
      </div>
      <div class="clock">4:21 PM</div>
      <div class="power">
        <svg width="14" height="22" viewBox="0 0 14 22" aria-hidden="true">
          <path d="M2 6 L12 15 L7 20 V2 L12 7 L2 16" fill="none" stroke="#a6ecd0" stroke-width="1.8"/>
        </svg>
        <span>100%</span>
        <span class="battery"><span></span></span>
      </div>
    </div>
    <svg class="menu-button" viewBox="0 0 50 50" role="img" aria-label="Menu">
      <circle cx="25" cy="25" r="23.5" fill="none" stroke="#fff" stroke-width="2"/>
      <path d="M16 19 H34 M16 25 H34 M16 31 H34" stroke="#fff" stroke-width="2"/>
    </svg>
    <h1 class="page-title">My Exams</h1>
  </header>

  <ul class="exam-list">
    <li class="exam-card" style="top:0">
      <svg class="progress-ring" viewBox="0 0 100 100" aria-hidden="true"><use href="#ring"/><circle cx="50" cy="50" r="43" fill="none" stroke="url(#arc-fill)" stroke-width="8" stroke-dasharray="32.4 270.2" transform="rotate(-90 50 50)"/></svg>
      <span class="progress-value">12%</span>
      <span class="exam-title">Skin and Soft Tissue</span>
      <span class="exam-status">15 of 125 answered</span>
      <svg class="exam-action" role="img" aria-label="Open"><use href="#chevron"/></svg>
    </li>
    <li class="exam-card" style="top:132px">
      <svg class="progress-ring" viewBox="0 0 100 100" aria-hidden="true"><use href="#ring"/><circle cx="50" cy="50" r="43" fill="none" stroke="url(#arc-fill)" stroke-width="8"/></svg>
      <span class="progress-value">100%</span>
      <span class="exam-title">Self-Assesstment 2006</span>
      <span class="exam-status">Submitted</span>
      <svg class="exam-action" role="img" aria-label="Open"><use href="#chevron"/></svg>
    </li>
    <li class="exam-card" style="top:263px">
      <svg class="progress-ring" viewBox="0 0 100 100" aria-hidden="true"><use href="#ring"/><circle cx="50" cy="50" r="43" fill="none" stroke="url(#arc-fill)" stroke-width="8" stroke-dasharray="135.1 270.2" transform="rotate(-90 50 50)"/></svg>
      <span class="progress-value">50%</span>
      <span class="exam-title">Self-Assesstment 2005</span>
      <span class="exam-status">63 of 125 answered</span>
      <svg class="exam-action" role="img" aria-label="Download"><use href="#download"/></svg>
    </li>
    <li class="exam-card" style="top:395px">
      <svg class="progress-ring" viewBox="0 0 100 100" aria-hidden="true"><use href="#ring"/><circle cx="50" cy="50" r="43" fill="none" stroke="url(#arc-fill)" stroke-width="8" stroke-dasharray="167.5 270.2" transform="rotate(-90 50 50)"/></svg>
      <span class="progress-value">62%</span>
      <span class="exam-title">Parathyroid Surgery</span>
      <span class="exam-status">76 of 125 answered</span>
      <svg class="exam-action" role="img" aria-label="Open"><use href="#chevron"/></svg>
    </li>
    <li class="exam-card" style="top:527px">
      <svg class="progress-ring" viewBox="0 0 100 100" aria-hidden="true"><use href="#ring"/><circle cx="50" cy="50" r="43" fill="none" stroke="url(#arc-fill)" stroke-width="8"/></svg>
      <span class="progress-value">100%</span>
      <span class="exam-title">Brindle Mobile v1.3</span>
      <span class="exam-status">Submitted</span>
      <svg class="exam-action" role="img" aria-label="Download"><use href="#download"/></svg>
    </li>
    <li class="exam-card" style="top:659px">
      <svg class="progress-ring" viewBox="0 0 100 100" aria-hidden="true"><use href="#ring"/><circle cx="50" cy="50" r="43" fill="none" stroke="url(#arc-fill)" stroke-width="8" stroke-dasharray="67.5 270.2" transform="rotate(-90 50 50)"/></svg>
      <span class="progress-value">25%</span>
      <span class="exam-title">Skin and Soft Tissue</span>
      <span class="exam-status">32 of 125 answered</span>
      <svg class="exam-action" role="img" aria-label="Open"><use href="#chevron"/></svg>
    </li>
    <li class="exam-card" style="top:790px">
      <svg class="progress-ring" viewBox="0 0 100 100" aria-hidden="true"><use href="#ring"/><circle cx="50" cy="50" r="43" fill="none" stroke="url(#arc-fill)" stroke-width="8" stroke-dasharray="202.6 270.2" transform="rotate(-90 50 50)"/></svg>
      <span class="progress-value">75%</span>
      <span class="exam-title">Brindle Mobile Advanced Topics 2</span>
      <span class="exam-status">93 of 125 answered</span>
      <svg class="exam-action" role="img" aria-label="Download"><use href="#download"/></svg>
    </li>
    <li class="exam-card" style="top:922px">
      <svg class="progress-ring" viewBox="0 0 100 100" aria-hidden="true"><use href="#ring"/><circle cx="50" cy="50" r="43" fill="none" stroke="url(#arc-fill)" stroke-width="8" stroke-dasharray="32.4 270.2" transform="rotate(-90 50 50)"/></svg>
      <span class="progress-value">12%</span>
      <span class="exam-title">Hip Arthrospcopy Essentials</span>
      <span class="exam-status">15 of 125 answered</span>
      <svg class="exam-action" role="img" aria-label="Download"><use href="#download"/></svg>
    </li>
  </ul>
</main>
</body>
</html>
```